Exciting & Elegant Stationary Pack

Stationary consists of
1. Letter head / Envelope
2. Business Card
3. Invoice
4. 40x40mm sticker

Attached files;

1. Logo (Other formats available on request)
2. MS word Doc - For information and description of design
3. Website image (This will be our new website so use the colours so everything ties together)
4. Sample of stationary pack we like, but feel free to be creative

Target Market(s)

Home improvement

Industry/Entity Type

Construction

Other font styles liked:
• Leave up to designer - We like font used on (website attached image)

Requirements
Must have
• Please look at uploaded file of sample website and use colours
Nice to have
• Any type of business card design - eg. metal, die cut, embossed, etc...

```html
<!DOCTYPE html>
<html lang="en">
<head>
<meta charset="utf-8">
<title>Grout &amp; Grid – Business Card</title>
<link rel="stylesheet" href="https://fonts.googleapis.com/css2?family=PT+Sans+Narrow:wght@400;700&family=Source+Sans+3:wght@400;700&display=swap">
<style>
  :root {
    --backdrop: #6b6b6b;
    --card-blue: #a4c8e6;
    --tile-blue: #9fc3e2;
    --band-red: #cc2229;
    --navy: #0d3a5f;
    --ink: #1b1b1b;
    --white: #ffffff;
  }
  * { margin: 0; padding: 0; box-sizing: border-box; }
  html, body {
    width: 1200px;
    height: 1037px;
    overflow: hidden;
    background: var(--backdrop);
  }
  .canvas { position: relative; width: 1200px; height: 1037px; }

  .card {
    position: absolute;
    width: 638px;
    height: 364px;
    background: var(--card-blue);
    overflow: hidden;
  }
  .card--front { left: 159px; top: 144px; }
  .card--back  { left: 391px; top: 570px; }

  .wordmark {
    position: absolute;
    display: flex;
    align-items: center;
    gap: 10px;
    font-family: "Source Sans 3", sans-serif;
    font-weight: 700;
    color: var(--navy);
    white-space: nowrap;
    letter-spacing: 0.5px;
  }
  .wordmark__square { width: 0.7em; height: 0.7em; background: var(--navy); }
  .card--front .wordmark { left: 36px; top: 66px; font-size: 38px; }
  .card--back .wordmark  { left: 280px; top: 168px; font-size: 40px; }

  .name-band {
    position: absolute;
    left: 0; top: 165px;
    width: 100%; height: 65px;
    background: var(--band-red);
    color: var(--white);
    text-align: right;
    padding: 9px 42px 0 0;
    font-family: "PT Sans Narrow", sans-serif;
  }
  .name-band__name  { font-size: 21px; font-weight: 700; line-height: 24px; }
  .name-band__title { font-size: 15px; line-height: 18px; }

  .contact {
    position: absolute;
    right: 40px; top: 246px;
    list-style: none;
    font-family: "Source Sans 3", sans-serif;
    font-size: 16px;
    color: var(--ink);
  }
  .contact__item {
    display: flex;
    justify-content: flex-end;
    align-items: center;
    gap: 10px;
    height: 24.5px;
  }
  .contact__icon { width: 18px; height: 18px; flex: none; }
  .contact__item--licence { padding-right: 28px; }

  .tile-field {
    position: absolute;
    inset: 0;
    background: var(--tile-blue);
  }
</style>
</head>
<body>
<main class="canvas">

  <section class="card card--front" aria-label="Business card front">
    <div class="wordmark"><span class="wordmark__square"></span>GROUT &amp; GRID</div>

    <div class="name-band">
      <p class="name-band__name">Linh Carter</p>
      <p class="name-band__title">Project Manager</p>
    </div>

    <ul class="contact">
      <li class="contact__item contact__item--licence">Lic No.,204719b</li>
      <li class="contact__item">0400 555 019
        <svg class="contact__icon" viewBox="0 0 18 18" aria-hidden="true">
          <rect x="5" y="1.5" width="8" height="15" rx="1.5" fill="none" stroke="#1b1b1b" stroke-width="1.8"/>
          <rect x="7.5" y="13.2" width="3" height="1.3" fill="#1b1b1b"/>
        </svg>
      </li>
      <li class="contact__item">hello@groutandgrid.com.au
        <svg class="contact__icon" viewBox="0 0 18 18" aria-hidden="true">
          <rect x="2" y="5" width="14" height="9" fill="#1b1b1b"/>
          <path d="M2 5 L9 10.5 L16 5" fill="none" stroke="#a4c8e6" stroke-width="1.2"/>
        </svg>
      </li>
      <li class="contact__item">www.groutandgrid.com.au
        <svg class="contact__icon" viewBox="0 0 18 18" aria-hidden="true">
          <circle cx="9" cy="9" r="7" fill="#1b1b1b"/>
          <path d="M5 7 Q8 5 9 8 T13 11" fill="none" stroke="#a4c8e6" stroke-width="1.2"/>
        </svg>
      </li>
    </ul>
  </section>

  <section class="card card--back" aria-label="Business card back">
    <div class="tile-field" role="img" aria-label="Light blue tiled wall pattern"></div>
    <div class="wordmark"><span class="wordmark__square"></span>GROUT &amp; GRID</div>
  </section>

</main>
</body>
</html>
```